IT supplier clean wordpress website - payment guaranteed

Clean website design for a wordpress based website
Design only - PSD delivery with images

current website: www.quilmo.net
please use your imagination and try something out of the box...
We like https://trevanly.com.au as look and feel, but you don't have to copy it, you can be creative

We like the navigation header and the phone number, but do not need 'instant quote' so the 1300 phone number and the 'lock' icon for login can be on the same line

Site Map:
IT support
VoIP
Internet and Data
Cloud hosting
About
Contact

Our logo is attached, it can be used light or dark.
Our only color used is the warm grey Pantone 8003C hex #877A69

You will only need to design the homepage to win the competition, but the winning designer will be required to supply without extra charges:
1. Home page design
2. A second, standard page template design
3. An icon set in colors appropriate to the site that have icons to match the subjects in these pages:
https://trevanly.com.au/products/
https://trevanly.com.au/making-the-switch/
https://trevanly.com.au/why-trevanly/
We will create a single page version of the options on https://trevanly.com.au/solutions/
4.Any images used

Please avoid stock photos that are too common - e.g. smiling woman with headset, try to make the design stand out with simple images and well-designed layout.

Mid-size business clients

It Company

1 page

• Quil logo
• Use Quil color

```html
<!DOCTYPE html>
<html lang="en">
<head>
<meta charset="utf-8">
<title>Quil — IT Outsourcing</title>
<link href="https://fonts.googleapis.com/css2?family=Lato:wght@400;700&family=Open+Sans:wght@400&family=Roboto:wght@700&family=Montserrat:wght@600;700&display=swap" rel="stylesheet">
<style>
  :root {
    --brand-grey: #877A69;
    --accent: #F5A623;
    --ink: #111111;
    --text: #333333;
    --muted: #8a8a8a;
    --soft: #f0f0f0;
    --alert: #E8413A;
    --white: #ffffff;
  }
  * { margin: 0; padding: 0; box-sizing: border-box; }
  html, body { width: 1200px; height: 1200px; overflow: hidden; background: var(--white); }
  body { position: relative; font-family: 'Lato', sans-serif; color: var(--text); }

  .site-header { position: absolute; left: 0; top: 0; width: 1200px; height: 122px; }
  .brand { position: absolute; left: 173px; top: 40px; display: flex; align-items: center; gap: 10px; }
  .brand-mark { width: 14px; height: 14px; background: var(--brand-grey); }
  .brand-name { font-family: 'Lato', sans-serif; font-size: 32px; font-weight: 400;
    color: var(--brand-grey); line-height: 1; }

  .call-us { position: absolute; left: 353px; top: 20px; display: flex; align-items: center; gap: 10px;
    font-size: 13px; color: var(--ink); }
  .call-us .icon { width: 26px; height: 26px; border-radius: 50%; background: var(--alert);
    display: flex; align-items: center; justify-content: center; }
  .call-us strong { font-weight: 700; }

  .account { position: absolute; top: 18px; left: 838px; display: flex; gap: 11px; }
  .btn { height: 28px; display: flex; align-items: center; gap: 8px; padding: 0 13px;
    font-size: 11px; color: var(--white); text-transform: uppercase; }
  .btn-login { width: 80px; background: var(--accent); }
  .btn-register { width: 97px; background: var(--ink); }

  .main-nav { position: absolute; left: 362px; top: 77px; display: flex; gap: 25px;
    font-size: 16.5px; color: var(--ink); }

  .hero { position: absolute; left: 0; top: 122px; width: 1200px; height: 455px;
    background: linear-gradient(100deg, #0d1c5c 0%, #1d3a8f 25%, #2142a0 45%, #1b3478 65%, #2a3a86 85%, #4a3a70 100%); }
  .hero-title { position: absolute; left: 0; top: 145px; width: 1200px; text-align: center;
    font-family: 'Roboto', sans-serif; font-weight: 700; font-size: 46px; color: var(--white); letter-spacing: -0.5px; }
  .hero-title span { color: var(--accent); }
  .hero-lead { position: absolute; left: 150px; top: 218px; width: 900px; text-align: center;
    font-family: 'Open Sans', sans-serif; font-size: 23.5px; line-height: 28px; color: var(--white); white-space: nowrap; }
  .scroll-cue { position: absolute; left: 586px; top: 396px; }

  .section-title { position: absolute; left: 0; width: 1200px; text-align: center;
    font-family: 'Montserrat', sans-serif; font-weight: 700; font-size: 27px; letter-spacing: 7px; color: var(--ink); }
  .section-title span { color: var(--accent); }
  .about-title { top: 632px; }
  .services-title { top: 1158px; }

  .about-text { position: absolute; left: 100px; top: 697px; width: 1000px; text-align: center;
    font-family: 'Open Sans', sans-serif; font-size: 14.4px; line-height: 23.5px; color: var(--text);
    letter-spacing: -0.4px; white-space: nowrap; }

  .features { position: absolute; left: 0; top: 852px; width: 1200px; }
  .feature { position: absolute; width: 200px; text-align: center; }
  .feature svg { display: block; margin: 0 auto; }
  .feature-label { margin-top: 52px; font-family: 'Montserrat', sans-serif; font-weight: 600;
    font-size: 13px; letter-spacing: 3.5px; color: var(--muted); text-transform: uppercase; white-space: nowrap; }
  .feature.is-active .feature-label { color: var(--ink); }
</style>
</head>
<body>

<header class="site-header">
  <div class="brand"><span class="brand-mark"></span><span class="brand-name">Quil</span></div>

  <div class="call-us">
    <span class="icon">
      <svg width="14" height="14" viewBox="0 0 24 24" fill="none" stroke="#fff" stroke-width="2">
        <path d="M5 3h4l2 5-3 2a12 12 0 0 0 6 6l2-3 5 2v4a2 2 0 0 1-2 2A17 17 0 0 1 3 5a2 2 0 0 1 2-2z"/>
      </svg>
    </span>
    <span><strong>Call us</strong> +02 5550 1234</span>
  </div>

  <div class="account">
    <a class="btn btn-login">
      <svg width="11" height="12" viewBox="0 0 11 12" fill="none" stroke="#fff" stroke-width="1.3">
        <path d="M4 1h6v10H4M1 6h6M5 4l2 2-2 2"/>
      </svg>Login</a>
    <a class="btn btn-register">
      <svg width="10" height="10" viewBox="0 0 10 10" stroke="#fff" stroke-width="1.6"><path d="M5 0v10M0 5h10"/></svg>Register</a>
  </div>

  <nav class="main-nav">
    <a>Home</a><a>IT Support</a><a>VoIP</a><a>Internet and Data</a><a>Cloud Hosting</a><a>About</a><a>Contact Us</a>
  </nav>
</header>

<section class="hero" role="img" aria-label="Data centre aisle with server racks lit in blue">
  <h1 class="hero-title">THE BEST <span>IT OUTSOURCING</span></h1>
  <p class="hero-lead">Lorem ipsum dolor sit amet, consectetur adipiscing elit. In luctus nisi<br>nisi, et faucibus diam facilisis et. Vestibulum nisl mauris, luctus vel ante<br>vel, feugiat interdum enim.</p>
  <svg class="scroll-cue" width="28" height="42" viewBox="0 0 28 42">
    <rect x="1" y="1" width="26" height="40" rx="13" fill="#fff" stroke="#222" stroke-width="1.5"/>
    <rect x="11.5" y="22" width="5" height="9" rx="2.5" fill="none" stroke="#222" stroke-width="1.3"/>
    <path d="M14 31v6" stroke="#222" stroke-width="1.3"/>
  </svg>
</section>

<h2 class="section-title about-title">ABOUT <span>US</span></h2>
<p class="about-text">Lorem ipsum dolor sit amet, consectetur adipiscing elit. Praesent eu nisi ac mi malesuada vestibulum. Phasellus tempor nunc<br>eleifend cursus molestie. Mauris lectus arcu, pellentesque at sodales sit amet, condimentum id nunc. Donec ornare mattis suscipit.<br>Praesent fermentum accumsan vulputate. Sed velit nulla, sagittis non erat id, dictum vestibulum ligula. Maecenas sed enim sem.</p>

<div class="features">
  <div class="feature" style="left:170px">
    <svg width="150" height="150" viewBox="0 0 150 150">
      <circle cx="75" cy="75" r="70" fill="none" stroke="#999" stroke-width="2" stroke-dasharray="12 8"/>
      <circle cx="75" cy="75" r="66" fill="var(--soft)"/>
      <g fill="#999">
        <circle cx="54" cy="64" r="9"/><path d="M38 95c0-14 6-20 16-20s16 6 16 20z"/>
        <circle cx="96" cy="64" r="9"/><path d="M80 95c0-14 6-20 16-20s16 6 16 20z"/>
        <circle cx="75" cy="60" r="11"/><path d="M56 98c0-17 7-24 19-24s19 7 19 24z"/>
      </g>
    </svg>
    <div class="feature-label">Right People</div>
  </div>

  <div class="feature is-active" style="left:392px">
    <svg width="150" height="150" viewBox="0 0 150 150">
      <circle cx="75" cy="75" r="73" fill="none" stroke="#111" stroke-width="2" stroke-dasharray="12 9"/>
      <path d="M70 36h40v74H62V52z" fill="#111"/>
      <circle cx="86" cy="56" r="10" fill="none" stroke="#fff" stroke-width="5" stroke-dasharray="5 3"/>
      <circle cx="86" cy="56" r="4" fill="#fff"/>
      <circle cx="54" cy="88" r="23" fill="#fff"/>
      <circle cx="54" cy="88" r="20" fill="#111"/>
      <circle cx="54" cy="88" r="8" fill="#fff"/>
      <circle cx="54" cy="88" r="4" fill="#111"/>
    </svg>
    <div class="feature-label">Right Software</div>
  </div>

  <div class="feature" style="left:608px">
    <svg width="150" height="150" viewBox="0 0 150 150">
      <circle cx="75" cy="75" r="72" fill="none" stroke="#999" stroke-width="2" stroke-dasharray="12 8"/>
      <circle cx="75" cy="75" r="67" fill="var(--soft)"/>
      <g fill="none" stroke="#999">
        <circle cx="72" cy="72" r="22" stroke-width="10" stroke-dasharray="8 6"/>
        <circle cx="72" cy="72" r="14" stroke-width="8"/>
      </g>
      <path d="M60 58l36 36" stroke="#999" stroke-width="8" stroke-linecap="round"/>
      <circle cx="58" cy="56" r="8" fill="#999"/>
      <circle cx="98" cy="96" r="6" fill="#999"/>
    </svg>
    <div class="feature-label">Right Support</div>
  </div>

  <div class="feature" style="left:827px">
    <svg width="150" height="150" viewBox="0 0 150 150">
      <circle cx="75" cy="75" r="70" fill="none" stroke="#999" stroke-width="2" stroke-dasharray="12 8"/>
      <circle cx="75" cy="75" r="66" fill="var(--soft)"/>
      <g fill="#999">
        <path d="M58 56a17 17 0 0 1 34 0h3v5H55v-5z"/>
        <path d="M62 63h26v6a13 13 0 0 1-26 0z"/>
        <path d="M48 106c0-16 10-24 27-24s27 8 27 24z"/>
      </g>
      <path d="M62 90l26 16M88 90l-26 16" stroke="var(--soft)" stroke-width="5" stroke-linecap="round"/>
    </svg>
    <div class="feature-label">Right Technicians</div>
  </div>
</div>

<h2 class="section-title services-title">OUR <span>SERVICES</span></h2>

</body>
</html>
```